Become a Mentor - For Musicians, Artists, Producers and Teachers

Here is the full creative brief:

https://files.plenwick.com/sheets/d/4kTqpLm8Wz_2RNa7Hc3Xv91Jd0Gb5YeUsQ6fNo8rTpxa/view?mode=shared

Here is the background image file: https://www.trovecrate.com/sh/83jbwtrmq5dkx2u/BBHn4k7QTf2ZpLeXX-wr9MUHe?dl=0

LOGO:
https://www.trovecrate.com/sh/k472rufmpdo9b6w/BBKLe3RtHY5J-sFQnLZw7Ggma?dl=0

```html
<!DOCTYPE html>
<html lang="en">
<head>
<meta charset="utf-8">
<title>Become a Mentor – Meridian Sound Academy</title>
<link rel="stylesheet" href="https://fonts.googleapis.com/css2?family=Montserrat:wght@300;400;500;600;700&family=Lobster&display=swap">
<style>
  :root {
    --navy: #0e0b52;
    --navy-deep: #0a0840;
    --royal: #0a22c4;
    --pink: #f08af7;
    --pink-light: #f5a6fa;
    --magenta: #ec5cf2;
    --white: #ffffff;
    --paper: #f2f3f2;
  }
  * { margin: 0; padding: 0; box-sizing: border-box; }
  html, body { width: 848px; height: 1200px; overflow: hidden; background: var(--pink); }
  .poster {
    position: relative;
    width: 848px;
    height: 1200px;
    overflow: hidden;
    font-family: "Montserrat", sans-serif;
    color: var(--navy);
  }
  .studio-photo {
    position: absolute;
    inset: 0 0 auto 0;
    height: 820px;
    background:
      radial-gradient(ellipse at 70% 30%, #6a5a8c 0%, transparent 55%),
      radial-gradient(ellipse at 15% 45%, #9c8aa6 0%, transparent 50%),
      linear-gradient(180deg, #5b4f7e 0%, #3d3470 45%, #1d1858 75%, var(--navy-deep) 100%);
  }
  .waves { position: absolute; left: 0; top: 700px; width: 848px; height: 500px; }
  .audience-tab {
    position: absolute;
    left: 271px; top: 0;
    width: 282px; height: 340px;
    background: var(--pink-light);
    border-radius: 0 0 80px 80px;
  }
  .audience-tab::after {
    content: "";
    position: absolute;
    left: 0; top: 0; right: 12px; bottom: 22px;
    background: var(--pink);
    border-radius: 0 0 78px 78px;
  }
  .audience-list {
    position: absolute;
    left: 309px; top: 58px;
    z-index: 2;
    font-weight: 300;
    font-size: 37px;
    line-height: 43px;
    color: var(--navy);
  }
  .frame {
    position: absolute;
    left: 30px; top: 30px;
    width: 788px; height: 1142px;
    border: 6px solid var(--white);
    pointer-events: none;
  }
  .brand {
    position: absolute;
    left: 632px; top: 84px;
    display: flex; align-items: center; gap: 8px;
    font-weight: 700;
    font-size: 15px;
    line-height: 17px;
    letter-spacing: 1px;
    color: var(--white);
  }
  .brand-dot { width: 14px; height: 14px; border-radius: 50%; background: var(--white); flex: none; }
  .tagline-band {
    position: absolute;
    left: 72px; top: 530px;
    width: 706px; height: 76px;
    background: var(--paper);
    border-radius: 30px;
  }
  .tagline {
    position: absolute;
    left: 0; width: 848px; top: 528px;
    text-align: center;
    font-family: "Lobster", cursive;
    font-size: 54px;
    line-height: 76px;
    color: var(--navy);
  }
  .headline-top {
    position: absolute;
    left: 56px; top: 618px;
    font-weight: 600;
    font-size: 102px;
    line-height: 1;
    letter-spacing: -3px;
    color: var(--white);
  }
  .headline-main {
    position: absolute;
    left: 58px; top: 700px;
    font-weight: 500;
    font-size: 167px;
    line-height: 1;
    letter-spacing: -3px;
    color: var(--magenta);
  }
  .pitch {
    position: absolute;
    left: 103px; top: 900px;
    font-weight: 600;
    font-size: 43px;
    line-height: 47px;
    letter-spacing: -1px;
    color: var(--navy);
  }
  .pitch span { display: block; padding-left: 6px; }
  .pitch span:first-child { padding-left: 0; }
  .divider {
    position: absolute;
    left: 106px; top: 1014px;
    width: 650px; height: 5px;
    border-radius: 3px;
    background: var(--navy);
  }
  .apply-button {
    position: absolute;
    left: 101px; top: 1037px;
    width: 251px; height: 76px;
    border-radius: 38px;
    background: var(--navy);
    color: var(--white);
    font-weight: 600;
    font-size: 31px;
    letter-spacing: -1px;
    display: flex; align-items: center; justify-content: center;
  }
  .phone-icon { position: absolute; left: 380px; top: 1040px; width: 64px; height: 64px; }
  .phone-number {
    position: absolute;
    left: 466px; top: 1048px;
    font-weight: 600;
    font-size: 40px;
    line-height: 48px;
    letter-spacing: -1px;
  }
  .website {
    position: absolute;
    left: 103px; top: 1120px;
    font-weight: 400;
    font-size: 22px;
    line-height: 28px;
    letter-spacing: 5.2px;
  }
</style>
</head>
<body>
<main class="poster">
  <div class="studio-photo" role="img" aria-label="Photo of two young musicians talking beside a mixing desk in a recording studio"></div>

  <svg class="waves" viewBox="0 0 848 500" preserveAspectRatio="none" aria-hidden="true">
    <rect x="0" y="0" width="848" height="500" fill="var(--navy-deep)"/>
    <path d="M0 100 C180 150 300 120 460 105 C620 90 760 80 848 100 L848 500 L0 500 Z" fill="var(--royal)"/>
    <path d="M0 115 C120 170 200 210 360 190 C520 170 680 150 848 200 L848 500 L0 500 Z" fill="var(--pink)"/>
  </svg>

  <div class="audience-tab"></div>
  <p class="audience-list">Designed for:<br>Musicians,<br>Artists,<br>Producers<br>&amp; Teachers.</p>

  <div class="brand">
    <span class="brand-dot"></span>
    <span>MERIDIAN<br>SOUND ACADEMY</span>
  </div>

  <div class="tagline-band"></div>
  <p class="tagline">Start your career today!</p>

  <h1>
    <span class="headline-top">BECOME A</span>
    <span class="headline-main">MENTOR</span>
  </h1>

  <p class="pitch"><span>Turn your skills and passion</span><span>for music into a career</span></p>

  <div class="divider"></div>

  <div class="apply-button">APPLY NOW!</div>

  <svg class="phone-icon" viewBox="0 0 24 24" aria-hidden="true">
    <path fill="var(--navy)" d="M6.6 10.8c1.4 2.8 3.8 5.1 6.6 6.6l2.2-2.2c.3-.3.7-.4 1-.2 1.1.4 2.3.6 3.6.6.6 0 1 .4 1 1V20c0 .6-.4 1-1 1C10.6 21 3 13.4 3 4c0-.6.4-1 1-1h3.5c.6 0 1 .4 1 1 0 1.3.2 2.5.6 3.6.1.3 0 .7-.2 1L6.6 10.8z"/>
  </svg>
  <p class="phone-number">1300 482 610</p>

  <p class="website">www.meridiansoundacademy.com.au</p>

  <div class="frame"></div>
</main>
</body>
</html>
```